Modern Business Card For A Digital Advertising Company

I'll be print on the Tarn Prints Velour paper http://us.tarnprints.example/products/velour/business-cards.html
Need's to be modern and use the color palette of the logo or gray scales. I think integrating the pixelation of the logo in to the card and having it wrap from one side to the other could be interesting. My company provides ad operations, web development, and number of other services to websites around the world. You can see my website at http://www.pixelharbor.example
Contact info on the card needs to have
Dana Welloby
President
p.555.318.4406
dana@pixelharbor.example
http://www.pixelharbor.example
Doesn't necessarily need to be in that order
Target Market(s)
Website owners
Industry/Entity Type
Business
Look and feel

```html
<!DOCTYPE html>
<html lang="en">
<head>
<meta charset="utf-8">
<title>Pixel Harbor — Business Card</title>
<link rel="stylesheet" href="https://fonts.googleapis.com/css2?family=Sorts+Mill+Goudy&display=swap">
<style>
  :root {
    --backdrop: #e4e4e2;
    --green-light: #b9e38f;
    --green-mid: #98d061;
    --green-text: #9be040;
    --band-black: #0b0c0c;
    --band-edge: #3a3a3a;
    --paper-top: #d9d9d9;
    --paper-bottom: #f7f7f7;
    --ink-dark: #1c1c1c;
    --icon-light: #f2f2f2;
  }
  * { margin: 0; padding: 0; box-sizing: border-box; }
  html, body {
    width: 922px; height: 1200px; overflow: hidden;
    background: var(--backdrop);
  }
  .canvas { position: relative; width: 922px; height: 1200px; }
  .card {
    position: absolute; left: 51px; top: 365px;
    width: 820px; height: 470px;
    border-radius: 14px; overflow: hidden;
    box-shadow: 0 6px 22px rgba(0,0,0,0.18);
    font-family: "Sorts Mill Goudy", Georgia, serif;
  }
  .card-art { position: absolute; inset: 0; }
  .brand {
    position: absolute; left: 48px; top: 52px;
    display: flex; align-items: center; gap: 14px;
  }
  .brand-square { width: 46px; height: 46px; background: var(--ink-dark); }
  .brand-name { font-size: 34px; color: var(--ink-dark); letter-spacing: 0.5px; }
  .identity {
    position: absolute; left: 520px; top: 90px; width: 260px;
    text-align: center; color: var(--green-text);
  }
  .identity-name { font-size: 31px; line-height: 1.1; }
  .identity-title { font-size: 22px; line-height: 1.3; }
  .contact-list { position: absolute; left: 470px; top: 180px; list-style: none; }
  .contact-item {
    display: flex; align-items: center; gap: 14px;
    height: 52px; color: var(--green-text); font-size: 22px;
  }
  .contact-icon { width: 38px; height: 38px; flex: none; }
  .phone {
    position: absolute; right: 38px; bottom: 38px;
    display: flex; align-items: center; gap: 12px;
    color: var(--ink-dark); font-size: 24px;
  }
  .phone-icon { width: 40px; height: 40px; }
</style>
</head>
<body>
<div class="canvas">
  <div class="card">
    <svg class="card-art" viewBox="0 0 820 470" width="820" height="470" aria-hidden="true">
      <defs>
        <linearGradient id="green-field" x1="0" y1="0" x2="0" y2="1">
          <stop offset="0" stop-color="var(--green-light)"/>
          <stop offset="1" stop-color="var(--green-mid)"/>
        </linearGradient>
        <linearGradient id="paper-field" x1="0" y1="0" x2="0" y2="1">
          <stop offset="0" stop-color="var(--paper-top)"/>
          <stop offset="1" stop-color="var(--paper-bottom)"/>
        </linearGradient>
      </defs>
      <rect width="820" height="470" fill="url(#paper-field)"/>
      <rect width="820" height="260" fill="url(#green-field)"/>
      <path class="band" d="M0,190 C110,218 190,205 250,135 C310,62 400,45 820,40 L820,300 C650,382 500,392 380,352 C260,308 150,268 0,282 Z"
            fill="var(--band-black)" stroke="var(--band-edge)" stroke-width="6"/>
    </svg>

    <div class="brand">
      <span class="brand-square"></span>
      <span class="brand-name">Pixel Harbor</span>
    </div>

    <div class="identity">
      <div class="identity-name">Dana Welloby</div>
      <div class="identity-title">President</div>
    </div>

    <ul class="contact-list">
      <li class="contact-item">
        <svg class="contact-icon" viewBox="0 0 38 38" aria-label="Address">
          <path d="M9,18 L19,8 L29,18 L29,30 L9,30 Z" fill="none" stroke="var(--icon-light)" stroke-width="2.5" stroke-linejoin="round"/>
        </svg>
        <span>Your Address Here</span>
      </li>
      <li class="contact-item">
        <svg class="contact-icon" viewBox="0 0 38 38" aria-label="Email">
          <rect x="3" y="3" width="32" height="32" rx="6" fill="#cfd3d6"/>
          <rect x="8" y="11" width="22" height="16" fill="none" stroke="#333" stroke-width="2"/>
          <path d="M8,11 L19,21 L30,11" fill="none" stroke="#333" stroke-width="2"/>
        </svg>
        <span>dana@pixelharbor.example</span>
      </li>
      <li class="contact-item">
        <svg class="contact-icon" viewBox="0 0 38 38" aria-label="Website">
          <g fill="none" stroke="var(--icon-light)" stroke-width="2">
            <circle cx="19" cy="19" r="14"/>
            <ellipse cx="19" cy="19" rx="6" ry="14"/>
            <line x1="5" y1="19" x2="33" y2="19"/>
            <line x1="19" y1="5" x2="19" y2="33"/>
            <path d="M8,11 H30 M8,27 H30"/>
          </g>
        </svg>
        <span>www.pixelharbor.example</span>
      </li>
    </ul>

    <div class="phone">
      <svg class="phone-icon" viewBox="0 0 40 40" aria-label="Phone">
        <circle cx="20" cy="20" r="17" fill="none" stroke="var(--ink-dark)" stroke-width="3"/>
        <path d="M14,11 L18,15 L16,18 C17,21 19,23 22,24 L25,22 L29,26 L26,29 C19,29 11,21 11,14 Z" fill="var(--ink-dark)"/>
      </svg>
      <span>555.318.4406</span>
    </div>
  </div>
</div>
</body>
</html>
```